Wordpress template re-design of current website

We need a WordPress template design and new look for our existing website. Our existing site it located at www.velmoro.com.au We are a tech company and want a fresh, clean modern website that matches our brand, services and logo colors. Our main Services are hospitality solutions, Velmoro TV solution and managed networks, more information on these can come from our existing website.

Target Market(s)

We are a tech company so must have a modern feel for new technology

Industry/Entity Type

It Company

Number of Pages Required

5+ page

Font styles to use
Sans Serif

Requirements
Must have
• Be based on a wordpress templete design and match the services that we have in our existing website, in the testimonials want a place for video testimonials as well as text. Nice clean icons used for graphics to represent services.
Nice to have
• nice visual representation of our services in the way of clean icons etc
Should not have
• Clutter

```html
<!DOCTYPE html>
<html lang="en">
<head>
<meta charset="utf-8">
<title>Velmoro Wireless</title>
<link rel="stylesheet" href="https://fonts.googleapis.com/css2?family=Lato:ital,wght@0,300;0,400;0,700;1,300;1,400;1,700&family=Roboto:wght@400;500;700&display=swap">
<style>
:root{
  --brand:#0b4a8f;
  --brand-bright:#1e73c8;
  --ink:#222;
  --muted:#8a8a8a;
  --white:#fff;
  --hero-dark:#0b0b0c;
}
*{margin:0;padding:0;box-sizing:border-box}
html,body{width:1200px;height:1200px;overflow:hidden;background:var(--white);font-family:'Lato',sans-serif;color:var(--ink)}
.page{position:relative;width:1200px;height:1200px;overflow:hidden;border-top:3px solid var(--brand)}
.site-header{height:93px;position:relative}
.brand{position:absolute;left:160px;top:24px;display:flex;align-items:center;gap:10px}
.brand-name{font-family:'Lato',sans-serif;font-size:36px;font-weight:400;color:var(--brand)}
.brand-dot{width:14px;height:14px;border-radius:50%;background:var(--brand)}
.main-nav{position:absolute;right:288px;top:42px;display:flex;gap:11px;font-family:'Roboto',sans-serif;font-size:11px;letter-spacing:.2px}
.main-nav a{color:var(--ink);text-decoration:none}
.main-nav a.is-current{color:var(--brand)}
.btn-start{position:absolute;left:931px;top:29px;width:109px;height:33px;background:var(--brand);color:var(--white);border-radius:3px;font-family:'Roboto',sans-serif;font-weight:700;font-size:12px;display:flex;align-items:center;justify-content:center}
.hero{position:absolute;top:96px;left:0;width:1200px;height:491px;background:radial-gradient(ellipse at 50% 60%,#2a2a2e 0%,#141416 55%,var(--hero-dark) 100%)}
.hero-title{position:absolute;top:180px;left:0;width:1200px;text-align:center;color:var(--white);font-style:italic;font-weight:300;font-size:34px;line-height:38px}
.hero-title strong{font-weight:700}
.hero-actions{position:absolute;top:283px;left:419px;display:flex;gap:12px}
.hero-btn{height:42px;display:flex;align-items:center;justify-content:center;font-style:italic;font-size:17px;color:var(--white)}
.hero-btn.primary{width:180px;background:var(--brand-bright)}
.hero-btn.outline{width:156px;border:2px solid var(--white)}
.hero-arrow{position:absolute;left:778px;top:262px}
.slide-dots{position:absolute;left:1169px;top:202px;display:flex;flex-direction:column;gap:7px}
.slide-dots span{width:8px;height:8px;border-radius:50%;background:var(--white)}
.slide-dots span.active{background:none;border:2px solid var(--brand-bright);width:10px;height:10px;margin-left:-1px}
.clients{position:absolute;top:587px;left:0;width:1200px;height:83px;display:flex;align-items:center;justify-content:space-between;padding:0 160px;box-shadow:0 6px 8px -6px rgba(0,0,0,.12)}
.client{font-family:'Lato',sans-serif;font-weight:700;font-size:15px;color:#555;letter-spacing:.5px}
.intro{position:absolute;top:748px;left:0;width:1200px;text-align:center}
.intro h2{font-size:26px;font-weight:700;color:var(--brand);margin-bottom:20px}
.intro p{width:670px;margin:0 auto;font-size:14px;line-height:20px;color:#333}
.intro p+p{margin-top:20px}
.btn-about{display:inline-flex;margin-top:20px;width:156px;height:37px;background:var(--brand);color:var(--white);font-weight:700;font-size:12.5px;align-items:center;justify-content:center}
.service-card{position:absolute;top:1036px;width:310px;height:170px}
.card-hospitality{left:275px;background:linear-gradient(180deg,#3a1c1c 0%,#1c1c1c 20%,#161616 100%)}
.card-tv{left:616px;background:linear-gradient(90deg,#e9e5df 0%,#c7c2bb 45%,#4f4a48 70%,#6b6560 100%)}
.card-label{position:absolute;left:72px;top:66px;width:162px;height:29px;border-top:2px solid var(--white);border-bottom:2px solid var(--white);color:var(--white);font-weight:700;font-size:12.6px;letter-spacing:-.2px;white-space:nowrap;text-align:center;line-height:25px}
</style>
</head>
<body>
<div class="page">
  <header class="site-header">
    <div class="brand"><span class="brand-name">Velmoro</span><span class="brand-dot"></span></div>
    <nav class="main-nav">
      <a class="is-current" href="#">HOME</a><a href="#">SERVICES</a><a href="#">ABOUT</a><a href="#">OUR WORK</a><a href="#">CONTACT</a><a href="#">PORTAL</a>
    </nav>
    <div class="btn-start">GET STARTED</div>
  </header>

  <section class="hero" role="img" aria-label="Dimmed photo of a hand using a tablet screen full of app icons">
    <h1 class="hero-title"><strong>Velmoro Wireless</strong> is at the forefront of revolutionising<br>high-speed internet access (HSIA) services.</h1>
    <div class="hero-actions">
      <div class="hero-btn primary">Learn more about Us</div>
      <div class="hero-btn outline">Try it yourself</div>
    </div>
    <svg class="hero-arrow" width="50" height="50" viewBox="0 0 50 50" fill="none" stroke="#ddd" stroke-width="1.5">
      <path d="M44 2 C48 22 30 36 5 42"/><path d="M15 34 L5 42 L16 45"/>
    </svg>
    <div class="slide-dots"><span class="active"></span><span></span><span></span><span></span><span></span></div>
  </section>

  <div class="clients">
    <span class="client">HARBOR</span>
    <span class="client">KESTREL</span>
    <span class="client">Lumina</span>
    <span class="client">Tourwide</span>
    <span class="client">Wattleby</span>
    <span class="client">Roamly</span>
    <span class="client">Brightore</span>
    <span class="client">Calmara Greens</span>
  </div>

  <section class="intro">
    <h2>Velmoro Wireless</h2>
    <p>We offer complete wireless solutions: Right from developing individual components such as hotspots and access controllers, to installation of the internet infrastructure. Once we setup the HSIA for our clients, we back it up with round-the-clock tech support.</p>
    <p>Velmoro’s expertise in wireless technology has attracted a growing client base from all over Australia.</p>
    <div class="btn-about">Learn more about Us</div>
  </section>

  <div class="service-card card-hospitality" role="img" aria-label="Dark photo of a hotel entrance at night">
    <div class="card-label">HOSPITALITY SOLUTIONS</div>
  </div>
  <div class="service-card card-tv" role="img" aria-label="Photo of a hotel room with a wall TV showing the guest menu"></div>
</div>
</body>
</html>
```